Business Card Design

My company is a Mobile RV Service,...we fix / repair / replace any
and all items on an RV that needs fixing or installing.....Our service goes to the customer, so they don't have to break down their rv from where ever they are at, and work on their unit in place. We also provide warranty service from the industry manufacturers who's products have been installed in the RV's. We also do insurance claims & repairs, & install items that the customer wants additionally installed ..ie: satellite systems, etc..
We accept cash, checks & especially ( all major credit cards )

Reason: 7:30 pm EST...USA,......Not sure how late people work in Australia,.....so ( 1 ) more day for a few finishing touches should be allowed......Thankyou, Dorwinel

Insurance

Bramblecrest Mobile RV Service 904-555-0162 Major credit cards
K.P.L.O. / K.P.E.N. Master Certified R.V. Technician
Licensed / Insured ( The " A " in Bramblecrest BOLD & RED ) also some kind of RV graphic somewhere on the card... The design has to sing !!!!.... Also design will be used for vehicle magnets or
vehicle wrap !!!!....

```html
<!DOCTYPE html>
<html lang="en">
<head>
<meta charset="utf-8">
<title>Bramblecrest Mobile RV Service – Business Card</title>
<link rel="stylesheet" href="https://fonts.googleapis.com/css2?family=Oswald:wght@500&family=Roboto:wght@400;500&family=Russo+One&display=swap">
<style>
  :root {
    --backdrop: #cfcfcf;
    --card-white: #ffffff;
    --brand-red: #d6181e;
    --brand-red-dark: #8e0e12;
    --card-black: #111111;
    --card-black-soft: #262626;
    --text-white: #ffffff;
    --text-black: #111111;
    --chip-bg: #ffffff;
    --chip-text: #1b1b1b;
  }
  * { box-sizing: border-box; margin: 0; padding: 0; }
  html, body {
    width: 1200px; height: 900px; overflow: hidden;
    background: var(--backdrop);
  }
  .card {
    position: absolute; left: 100px; top: 165px;
    width: 1000px; height: 571px;
    border-radius: 40px; overflow: hidden;
    background: var(--card-black);
  }
  .card-top {
    position: absolute; left: 0; top: 0; width: 100%; height: 232px;
    background: var(--card-white);
  }
  .rv-graphic {
    position: absolute; left: 70px; top: 40px; width: 160px; height: 160px;
  }
  .brand-name {
    position: absolute; left: 262px; top: 48px;
    font-family: "Russo One", sans-serif;
    color: var(--brand-red);
    text-transform: uppercase; line-height: 1;
  }
  .brand-name .brand-main { display: block; font-size: 76px; letter-spacing: 1px; }
  .brand-name .brand-sub { display: block; font-size: 44px; margin-top: 12px; letter-spacing: 2px; }
  .cert-band {
    position: absolute; left: 0; top: 232px; width: 100%; height: 32px;
    background: linear-gradient(180deg, var(--brand-red) 0%, var(--brand-red-dark) 100%);
    display: flex; align-items: center; justify-content: center;
    font-family: "Roboto", sans-serif; font-weight: 500;
    font-size: 17px; letter-spacing: 4px; font-variant: small-caps;
    color: var(--text-black);
  }
  .card-bottom {
    position: absolute; left: 0; top: 264px; width: 100%; height: 307px;
    background: radial-gradient(ellipse at 50% 30%, var(--card-black-soft) 0%, var(--card-black) 70%);
  }
  .credentials {
    position: absolute; left: 0; top: 22px; width: 100%; text-align: center;
    font-family: "Roboto", sans-serif; font-weight: 500;
    font-size: 21px; letter-spacing: 4px; font-variant: small-caps;
    color: var(--brand-red);
  }
  .phone {
    position: absolute; left: 0; top: 62px; width: 100%; text-align: center;
    font-family: "Oswald", sans-serif; font-weight: 500;
    font-size: 54px; color: var(--text-white); line-height: 1.1;
  }
  .owner {
    position: absolute; left: 0; top: 130px; width: 100%; text-align: center;
    font-family: "Roboto", sans-serif; font-weight: 400;
    font-size: 22px; color: var(--text-white);
  }
  .payments {
    position: absolute; left: 0; top: 196px; width: 100%;
    display: flex; justify-content: center; gap: 10px;
  }
  .payment-chip {
    width: 70px; height: 48px; background: var(--chip-bg);
    display: flex; align-items: center; justify-content: center; text-align: center;
    font-family: "Roboto", sans-serif; font-weight: 500; font-size: 11px;
    color: var(--chip-text); line-height: 1.1;
  }
</style>
</head>
<body>
  <div class="card">
    <div class="card-top">
      <svg class="rv-graphic" viewBox="0 0 160 160" role="img" aria-label="Red RV motorhome illustration with a technician silhouette">
        <rect x="0" y="0" width="160" height="160" fill="#c8161c"/>
      </svg>
      <h1 class="brand-name">
        <span class="brand-main">Bramblecrest</span>
        <span class="brand-sub">Mobile RV Service</span>
      </h1>
    </div>
    <div class="cert-band">K.P.L.O. / K.P.E.N. Master Certified R.V. Technician</div>
    <div class="card-bottom">
      <p class="credentials">Licensed / Insured</p>
      <p class="phone">904-555-0162</p>
      <p class="owner">Dorwin Halloway</p>
      <div class="payments">
        <span class="payment-chip">Meridian</span>
        <span class="payment-chip">Vantor</span>
        <span class="payment-chip">Atlas Charge</span>
        <span class="payment-chip">Delvo</span>
      </div>
    </div>
  </div>
</body>
</html>
```